Webdesign for a Bikeshop in Innsbruck (submitted designs will be used for Masterthesis anonymously)

To obtain my master's degree, I am conducting a study in the field of web design as part of my master thesis. All submitted designs will therefore be used for study purposes. In order to achieve a homogeneous group, I would like to encourage not only male but also female web designers to submit a design. All submitted designs will be used anonymously for the study and therefore do not allow any conclusions to be drawn about your person. Since this is a contest, the winner will be chosen randomly from all serious submissions. I would be really happy if you would support me in my study. I think the results could be very informative and also useful for your further work (I won't go into more detail here as it could skew the results - but once the contest is over, feel free to contact me. Of course I will also provide you with my results as soon as my work is finished). Below you will find a usecase and a description of what the website should include:

The company Pedalwerk Almhof is planning to relaunch its own website and would like to present itself primarily as a competent and leading consultant in the field of cargo bikes. The design should appeal to a broad audience and embody an urban lifestyle. In any case, the website should include a landing page, a product overview page and a product details page, also make sure to design as gender neutral as possible. You only design the website. So don't worry about hardware or software limitations, just create the best bike store design you can.

Number of Pages Required

1 page

Requirements
Must have
• landing page, product overview page, product details page
Should not have
• onlineshop

```html
<!DOCTYPE html>
<html lang="en">
<head>
<meta charset="utf-8">
<title>Pedalwerk Almhof – Cargo Bikes</title>
<link rel="stylesheet" href="https://fonts.googleapis.com/css2?family=Oswald:wght@400;500&family=Poppins:wght@400;500;600&display=swap">
<style>
:root{
  --orange:#f9a21b;
  --dark:#333333;
  --ink:#2b2b2b;
  --text:#444444;
  --muted:#777777;
  --light:#f0f0f0;
  --white:#ffffff;
}
*{margin:0;padding:0;box-sizing:border-box}
html,body{width:1200px;height:3869px;overflow:hidden;background:var(--white)}
body{position:relative;font-family:'Poppins',sans-serif;color:var(--text)}
.abs{position:absolute}
.display{font-family:'Oswald',sans-serif;font-weight:500;color:var(--ink);text-transform:uppercase;line-height:1.05}
.btn{position:absolute;display:flex;align-items:center;justify-content:center;background:var(--orange);color:var(--white);font-weight:600;font-size:16px;height:48px;width:164px}
.body-copy{font-size:17px;line-height:31.5px;color:var(--text)}
.photo{position:absolute}

/* header */
.hero-panel{left:747px;top:0;width:453px;height:740px;background:var(--dark)}
.logo{left:75px;top:22px;font-size:46px}
.nav{left:470px;top:64px;display:flex;gap:0;font-size:13px;font-weight:500;color:#8a8a8a}
.nav a{position:absolute;white-space:nowrap;text-decoration:none;color:#8a8a8a}
.nav a.active{color:var(--ink)}
.nav a.on-dark{color:#bdbdbd}
.cart{left:1093px;top:62px}
.hero-photo{left:385px;top:90px;width:770px;height:725px;border-radius:48% 40% 44% 46%;background:radial-gradient(ellipse at 55% 45%,#c9a17a 0%,#d9d9d9 45%,rgba(220,220,220,0) 72%)}
.hero-title{left:75px;top:222px;font-size:57px}
.hero-title .accent{color:var(--orange)}
.hero-copy{left:75px;top:350px;width:420px}

/* about */
.about-photo{left:75px;top:900px;width:512px;height:490px;border-bottom-right-radius:200px;background:linear-gradient(150deg,#7a6a55 0%,#5d6a48 35%,#b9b59a 70%,#d8d8d8 100%)}
.about-title{left:616px;top:980px;font-size:48px}
.about-copy{left:616px;top:1100px;width:510px}

/* tabs */
.tabs{left:75px;top:1480px;width:1050px;height:63px;display:flex}
.tab{flex:1;display:flex;align-items:center;justify-content:center;background:var(--light);font-family:'Oswald',sans-serif;font-weight:500;font-size:29px;color:var(--ink);text-transform:uppercase}
.tab.active{background:var(--dark);color:var(--white)}
.product-photo{width:359px;height:297px}
.product-info{background:var(--white);width:290px;height:135px;padding:22px 24px}
.product-info h3{font-family:'Oswald',sans-serif;font-weight:500;font-size:26px;color:var(--ink);text-transform:uppercase}
.product-info p{font-size:17px;margin-top:6px;color:var(--text)}
.product-info .price{font-weight:600;color:var(--orange);margin-top:12px}

/* technology */
.tech-title{left:75px;top:2065px;font-size:48px}
.tech-copy{left:75px;top:2185px;width:520px}
.tech-photo{left:614px;top:1985px;width:511px;height:489px;border-bottom-left-radius:200px;background:linear-gradient(160deg,#a7a7a7 0%,#8e8e8e 40%,#b79a74 65%,#c9c23c 100%)}

/* testimonial */
.testimonial{left:0;top:2548px;width:1200px;height:414px;background:#f1f1f1;text-align:center}
.quote-mark{position:absolute;left:582px;top:60px;font-family:'Oswald',sans-serif;font-size:82px;color:var(--orange);line-height:1}
.quote-text{position:absolute;left:150px;top:118px;width:900px;font-size:19.5px;line-height:35px;color:var(--text)}
.quote-name{position:absolute;left:0;width:1200px;top:250px;font-family:'Oswald',sans-serif;font-size:18px;color:var(--ink)}
.dots{position:absolute;top:326px;left:556px;display:flex;gap:14px}
.dots span{width:12px;height:12px;border-radius:50%;background:#555}
.dots span.active{background:var(--orange)}

/* social */
.social-title{left:75px;top:3110px;font-size:48px}
.social-photo{top:3040px;height:245px}

/* footer */
.footer-panel{left:0;top:3378px;width:497px;height:491px;background:var(--dark);border-top-right-radius:160px}
.footer-logo{left:75px;top:3468px;font-size:46px;color:var(--white)}
.newsletter-label{left:75px;top:3600px;font-family:'Oswald',sans-serif;font-size:20px;color:var(--white);text-transform:uppercase}
.newsletter{left:75px;top:3642px;width:359px;height:51px;display:flex}
.newsletter .field{flex:1;background:var(--white);font-size:14px;color:var(--text);display:flex;align-items:center;padding-left:13px}
.newsletter .go{width:57px;background:var(--orange);display:flex;align-items:center;justify-content:center}
.copyright{left:75px;top:3724px;font-size:13.5px;line-height:26px;color:var(--white)}
.social-links{left:75px;top:3796px;display:flex;gap:19px}
.social-links span{width:17px;height:17px;border-radius:50%;background:var(--orange)}
.footer-col h4{font-size:16.5px;font-weight:600;color:var(--ink);text-transform:uppercase;margin-bottom:17px}
.footer-col a{display:block;font-size:13px;color:var(--text);text-decoration:none;text-transform:uppercase;line-height:41.5px}
.footer-col{top:3466px}
</style>
</head>
<body>

<!-- Header & hero -->
<div class="abs hero-panel"></div>
<div class="abs display logo">Pedalwerk<br>Almhof</div>
<nav class="abs nav" style="left:0;top:64px">
  <a class="active" style="left:470px">HOME</a>
  <a style="left:549px">ABOUT US</a>
  <a style="left:656px">PRODUCTS</a>
  <a class="on-dark" style="left:770px">FEATURES</a>
  <a class="on-dark" style="left:877px">REVIEWS</a>
  <a class="on-dark" style="left:975px">CONTACT</a>
</nav>
<svg class="abs cart" width="26" height="18" viewBox="0 0 26 18" aria-label="Cart">
  <path d="M2 6h14l-2 8H4z" fill="none" stroke="#fff" stroke-width="2"/>
  <path d="M5 6l4-5M13 6l-3-5" stroke="#fff" stroke-width="1.6"/>
  <text x="17" y="6" font-size="8" fill="#f9a21b" font-family="Poppins,sans-serif">(0)</text>
</svg>
<div class="photo hero-photo" role="img" aria-label="Courier riding a white cargo tricycle loaded with parcels"></div>
<h1 class="abs display hero-title"><span class="accent">Treandy &amp; Comfortable</span><br>Cargo Bikes</h1>
<p class="abs body-copy hero-copy">Sed ut perspiciatis unde omnis iste natus error sit &nbsp;voluptatem accusantium doloremque laudantium, totam rem aperiam.</p>
<div class="btn" style="left:75px;top:465px">SHOP NOW</div>

<!-- About -->
<div class="photo about-photo" role="img" aria-label="Cyclist on a yellow cargo bike carrying boxes across a city street"></div>
<h2 class="abs display about-title">About Pedalwerk<br>Almhof</h2>
<p class="abs body-copy about-copy">Sed ut perspiciatis unde omnis iste natus error sit voluptatem accusantium doloremque laudantium, totam rem aperiam, eaque ipsa quae ab illo inventore veritatis et quasi architecto beatae vitae dicta.</p>
<div class="btn" style="left:616px;top:1254px">Our History</div>

<!-- Products -->
<div class="abs tabs">
  <div class="tab">Accessories</div>
  <div class="tab active">Latest Collections</div>
  <div class="tab">Featured Items</div>
</div>
<svg class="abs" style="left:42px;top:1745px" width="18" height="30" viewBox="0 0 18 30"><path d="M15 2L3 15l12 13" fill="none" stroke="#777" stroke-width="2"/></svg>
<svg class="abs" style="left:1141px;top:1745px" width="18" height="30" viewBox="0 0 18 30"><path d="M3 2l12 13L3 28" fill="none" stroke="#777" stroke-width="2"/></svg>

<div class="photo product-photo" style="left:75px;top:1591px;background:linear-gradient(160deg,#8a6a55 0%,#d4661c 45%,#9a9a9a 100%)" role="img" aria-label="Cargo bike with an orange box parked by a brick wall"></div>
<div class="abs product-info" style="left:295px;top:1754px">
  <h3>Product Heading</h3>
  <p>Sed ut perspiciatis unde om</p>
  <p class="price">$250.00</p>
</div>
<div class="photo product-photo" style="left:616px;top:1591px;background:linear-gradient(160deg,#6f8a4a 0%,#4e6a38 40%,#c6a57e 75%,#8a8a8a 100%)" role="img" aria-label="Cyclist on a cargo bike loaded with parcels among green trees"></div>
<div class="abs product-info" style="left:834px;top:1754px">
  <h3>Product Heading</h3>
  <p>Sed ut perspiciatis unde om</p>
  <p class="price">$250.00</p>
</div>

<!-- Technology -->
<h2 class="abs display tech-title">Our Technology Used<br>in Cargobikes</h2>
<p class="abs body-copy tech-copy">Sed ut perspiciatis unde omnis iste natus error sit voluptatem accusantium doloremque laudantium, totam rem aperiam, eaque ipsa quae ab illo inventore veritatis et quasi architecto beatae vitae dicta.</p>
<div class="btn" style="left:75px;top:2338px">Our History</div>
<div class="photo tech-photo" role="img" aria-label="Rider checking a phone beside a yellow cargo bike stacked with boxes"></div>

<!-- Testimonial -->
<section class="abs testimonial">
  <div class="quote-mark">”</div>
  <p class="quote-text">“ Sed ut perspiciatis unde omnis iste natus error sit voluptatem accusantium doloremque laudantium, totam rem aperiam, eaque ipsa quae ab illo inventore veritatis et quasi architecto beatae vitae dicta sunt explicabo..”</p>
  <div class="quote-name">NAME HEADING</div>
  <div class="dots"><span class="active"></span><span></span><span></span><span></span></div>
</section>

<!-- Social wall -->
<h2 class="abs display social-title">Our Social Media<br>Wall</h2>
<div class="photo social-photo" style="left:434px;width:270px;background:linear-gradient(160deg,#6a5a48 0%,#7b8a48 45%,#b9b59a 100%)" role="img" aria-label="Cargo bike rider on a city street"></div>
<div class="photo social-photo" style="left:720px;width:270px;background:linear-gradient(160deg,#9a8a78 0%,#c98a3a 45%,#5a6a3a 100%)" role="img" aria-label="Family cargo bike carrying a small tree in autumn"></div>
<div class="photo social-photo" style="left:1005px;width:195px;background:linear-gradient(160deg,#7a6a58 0%,#8fa04a 50%,#a8a8a8 100%)" role="img" aria-label="Cyclist on a yellow cargo bike with parcels"></div>

<!-- Footer -->
<div class="abs footer-panel"></div>
<div class="abs display footer-logo">Pedalwerk<br>Almhof</div>
<div class="abs newsletter-label">Newsletter Signup</div>
<div class="abs newsletter">
  <div class="field">Enter Email Address</div>
  <div class="go">
    <svg width="26" height="26" viewBox="0 0 26 26"><circle cx="13" cy="13" r="11" fill="#fff"/><path d="M7 13h11M13 8l5 5-5 5" fill="none" stroke="#f9a21b" stroke-width="2.4"/></svg>
  </div>
</div>
<div class="abs copyright">Copyright © 2022 &nbsp;CompanyName<br>All Right Reserved</div>
<div class="abs social-links" aria-label="Social channels"><span></span><span></span><span></span><span></span><span></span></div>

<div class="abs footer-col" style="left:541px">
  <h4>Quick Links</h4>
  <a>Home</a><a>About Us</a><a>Products</a><a>Features</a><a>Reviews</a><a>Contact</a>
</div>
<div class="abs footer-col" style="left:748px">
  <h4>Support</h4>
  <a>Excepteur sint</a><a>Occaecat cupidatat</a><a>Non proident</a><a>Sunt in culpa qui</a><a>Officia deserunt</a><a>Mollit anim</a>
</div>
<div class="abs footer-col" style="left:961px">
  <h4>My Account</h4>
  <a>Excepteur sint</a><a>Occaecat cupidatat</a><a>Non proident</a><a>Sunt in culpa qui</a>
</div>

</body>
</html>
```